Simplified Double Diamond Diagram for Book

I need a simplified version of the Double Diamond Diagram for a book I am working on. I would like to represent the diagram with the following image/text:
- Two diamonds connected (as in each of the sample photos)
- Inclusion of "Diverge" "Converge" above each of the sides of the diamonds as shown in sample image 1 - without elaborative text
- Inclusion of "Problem" and "Solution" in each diamond as is shown in the example image 2
- I need a color version and black/white version of the image that can be turned into a mono-color version in the book.

```html
<!DOCTYPE html>
<html lang="en">
<head>
<meta charset="UTF-8">
<title>Double Diamond Diagram – Colour and Mono</title>
<link rel="stylesheet" href="https://fonts.googleapis.com/css2?family=Archivo+Black&family=Roboto:wght@700&display=swap">
<style>
  :root {
    --paper: #ffffff;
    --problem-band: #e8553a;
    --problem-ink: #e0262a;
    --problem-tint: #fbe1dc;
    --solution-band: #54a85a;
    --solution-ink: #1e9a44;
    --solution-tint: #dff0e1;
    --mono-band: #555354;
    --mono-ink: #3a3a3a;
    --mono-tint: #e6e6e6;
    --label-ink: #2f2f2f;
  }
  html, body {
    margin: 0;
    padding: 0;
    width: 1200px;
    height: 1200px;
    overflow: hidden;
    background: var(--paper);
  }
  .canvas {
    display: block;
    width: 1200px;
    height: 1200px;
  }
  .phase-label {
    font-family: "Roboto", Arial, sans-serif;
    font-weight: 700;
    font-size: 29px;
    fill: var(--label-ink);
    text-anchor: middle;
    letter-spacing: 0.5px;
  }
  .phase-title {
    font-family: "Archivo Black", "Arial Black", sans-serif;
    font-size: 29px;
    text-anchor: middle;
    letter-spacing: 0.5px;
  }
  .band { fill: none; stroke: currentColor; stroke-width: 32; stroke-linejoin: miter; }
  .inner-frame { fill: none; stroke: currentColor; stroke-width: 2; }
  .axis { stroke: currentColor; stroke-width: 2; stroke-dasharray: 14 12; }
  .overlap { opacity: 0.88; }
  .icon-area { stroke: none; }

  .colour .problem { color: var(--problem-band); }
  .colour .problem-detail { color: var(--problem-ink); }
  .colour .solution { color: var(--solution-band); }
  .colour .solution-detail { color: var(--solution-ink); }
  .colour .problem-title { fill: var(--problem-ink); }
  .colour .solution-title { fill: var(--solution-ink); }
  .colour .problem-icon { fill: var(--problem-tint); }
  .colour .solution-icon { fill: var(--solution-tint); }

  .mono .problem, .mono .solution { color: var(--mono-band); }
  .mono .problem-detail, .mono .solution-detail { color: var(--mono-ink); }
  .mono .problem-title, .mono .solution-title { fill: var(--mono-ink); }
  .mono .problem-icon, .mono .solution-icon { fill: var(--mono-tint); }
</style>
</head>
<body>
<svg class="canvas" viewBox="420 350 1100 1270" preserveAspectRatio="xMidYMid meet" xmlns="http://www.w3.org/2000/svg" role="img" aria-label="Double Diamond diagram in colour and in mono: Problem and Solution, each with Diverge and Converge sides">
  <defs>
    <symbol id="diamond-band" viewBox="-265 -265 530 530" overflow="visible">
      <polygon class="band" points="0,-240 240,0 0,240 -240,0"/>
    </symbol>
    <symbol id="diamond-inner" viewBox="-265 -265 530 530" overflow="visible">
      <polygon class="inner-frame" points="0,-198 198,0 0,198 -198,0"/>
      <line class="axis" x1="0" y1="-196" x2="0" y2="-75"/>
      <line class="axis" x1="0" y1="80" x2="0" y2="196"/>
    </symbol>

    <g id="diagram-labels">
      <text class="phase-label" transform="translate(624 452) rotate(-45)">DIVERGE</text>
      <text class="phase-label" transform="translate(836 458) rotate(45)">CONVERGE</text>
      <text class="phase-label" transform="translate(1101 452) rotate(-45)">DIVERGE</text>
      <text class="phase-label" transform="translate(1313 458) rotate(45)">CONVERGE</text>
    </g>
  </defs>

  <!-- colour version -->
  <g class="diagram colour">
    <use href="#diagram-labels"/>
    <g class="problem"><use href="#diamond-band" x="463" y="380" width="530" height="530"/></g>
    <g class="solution overlap"><use href="#diamond-band" x="942" y="380" width="530" height="530"/></g>
    <g class="problem-detail"><use href="#diamond-inner" x="463" y="380" width="530" height="530"/></g>
    <g class="solution-detail"><use href="#diamond-inner" x="942" y="380" width="530" height="530"/></g>
    <circle class="icon-area problem-icon" cx="730" cy="623" r="44" role="img" aria-label="Problem icon: search for an issue"/>
    <circle class="icon-area solution-icon" cx="1207" cy="623" r="44" role="img" aria-label="Solution icon: an idea"/>
    <text class="phase-title problem-title" x="738" y="716">PROBLEM</text>
    <text class="phase-title solution-title" x="1207" y="716">SOLUTION</text>
  </g>

  <!-- mono version -->
  <g class="diagram mono" transform="translate(0 680)">
    <use href="#diagram-labels"/>
    <g class="problem"><use href="#diamond-band" x="463" y="380" width="530" height="530"/></g>
    <g class="solution overlap"><use href="#diamond-band" x="942" y="380" width="530" height="530"/></g>
    <g class="problem-detail"><use href="#diamond-inner" x="463" y="380" width="530" height="530"/></g>
    <g class="solution-detail"><use href="#diamond-inner" x="942" y="380" width="530" height="530"/></g>
    <circle class="icon-area problem-icon" cx="730" cy="623" r="44" role="img" aria-label="Problem icon: search for an issue"/>
    <circle class="icon-area solution-icon" cx="1207" cy="623" r="44" role="img" aria-label="Solution icon: an idea"/>
    <text class="phase-title problem-title" x="738" y="716">PROBLEM</text>
    <text class="phase-title solution-title" x="1207" y="716">SOLUTION</text>
  </g>
</svg>
</body>
</html>
```